Business Card design for new private practice opening

I need a business card design for my new private practice with my new logo uploaded as a file
On the front the logo
On the back: maybe a small logo somewhere?
Priv. Doz. DDr. Petra Sommerfeld
Fachärztin für Allgemein- & Viszeralchirurgie
Address: xxx
Tel: xxx
Mobil:xxx
Webseite:xxx
Email:xxx

Contact Information for Business Card

See project description above for details

Requirements
Nice to have
• I would like the colors of the logo incorporated into the business card

```html
<!DOCTYPE html>
<html lang="de">
<head>
<meta charset="utf-8">
<title>Sommerfeld Chirurgie – Visitenkarte</title>
<link rel="stylesheet" href="https://fonts.googleapis.com/css2?family=Montserrat:wght@300;400;600;700&family=Poppins:wght@300;400&display=swap">
<style>
  :root {
    --teal: #47b8b6;
    --paper: #f8f8f8;
    --ink-grey: #7b7b7b;
    --logo-grey: #808080;
    --white: #ffffff;
    --backdrop: #e6e6e6;
  }
  * { box-sizing: border-box; margin: 0; padding: 0; }
  html, body { width: 1069px; height: 1200px; overflow: hidden; }
  body {
    background: var(--backdrop);
    position: relative;
    font-family: "Montserrat", sans-serif;
  }
  .card {
    position: absolute;
    left: 153px;
    width: 763px;
    height: 447px;
    overflow: hidden;
    box-shadow: 0 8px 30px rgba(0,0,0,0.12);
  }
  .card--front { top: 129px; background: var(--paper); }
  .card--back { top: 634px; background: var(--teal); }

  /* Front */
  .person { position: absolute; left: 20px; top: 42px; }
  .person__name {
    font-weight: 700; font-size: 21px; color: var(--teal);
    letter-spacing: 0.2px; white-space: nowrap;
  }
  .person__title {
    margin-top: 4px; font-weight: 400; font-size: 15.5px;
    color: var(--teal); white-space: nowrap;
  }
  .contact-tab {
    position: absolute; left: 0; top: 112px; width: 86px; height: 244px;
    background: var(--teal); border-radius: 0 28px 28px 0;
  }
  .contact-row {
    position: absolute; left: 0; height: 36px;
    display: flex; align-items: center;
  }
  .contact-row__icon { width: 86px; display: flex; justify-content: center; }
  .contact-row__icon svg { width: 20px; height: 20px; fill: var(--white); }
  .contact-row__text {
    margin-left: 12px; font-family: "Poppins", sans-serif; font-weight: 300;
    color: var(--ink-grey); white-space: nowrap;
  }
  .contact-row--big .contact-row__text { font-size: 28px; }
  .contact-row--small .contact-row__text { font-size: 25px; }

  .brand-small { position: absolute; left: 424px; top: 38px; display: flex; align-items: center; }
  .brand-small__mark {
    flex: none; width: 82px; height: 82px; border-radius: 50%;
    border: 3px solid var(--logo-grey);
  }
  .brand-small__name {
    margin-left: 13px; font-weight: 700; font-size: 29px; line-height: 1.17;
    color: var(--logo-grey); white-space: nowrap;
  }
  .front-band {
    position: absolute; left: 0; bottom: 0; width: 100%; height: 69px;
    background: var(--teal);
  }

  /* Back */
  .brand-large {
    position: absolute; left: 92px; top: 99px; display: flex; align-items: center;
  }
  .brand-large__mark {
    flex: none; width: 172px; height: 172px; border-radius: 50%;
    border: 5px solid var(--white);
  }
  .brand-large__name {
    margin-left: 24px; font-weight: 700; font-size: 60px; line-height: 1.17;
    color: var(--white); white-space: nowrap;
  }
  .back-rule {
    position: absolute; top: 339px; height: 5px; background: var(--white);
    border-radius: 3px;
  }
  .back-rule--left { left: -4px; width: 189px; }
  .back-rule--right { left: 581px; width: 190px; }
  .back-url {
    position: absolute; left: 0; width: 763px; top: 323px; text-align: center;
    font-family: "Poppins", sans-serif; font-weight: 300; font-size: 26px;
    color: var(--white); letter-spacing: 0.3px;
  }
</style>
</head>
<body>

<section class="card card--front">
  <div class="person">
    <p class="person__name">Priv. Doz. DDr. Petra Sommerfeld</p>
    <p class="person__title">Fachärztin für Allgemein- &amp; Viszeralchirurgie</p>
  </div>

  <div class="brand-small">
    <div class="brand-small__mark"></div>
    <p class="brand-small__name">SOMMERFELD<br>CHIRURGIE</p>
  </div>

  <div class="contact-tab"></div>

  <div class="contact-row contact-row--big" style="top:127px">
    <span class="contact-row__icon">
      <svg viewBox="0 0 24 24"><path d="M7 1h10a2 2 0 0 1 2 2v18a2 2 0 0 1-2 2H7a2 2 0 0 1-2-2V3a2 2 0 0 1 2-2zm0 4v13h10V5zm5 14.5a1 1 0 1 0 0 2 1 1 0 0 0 0-2z"/></svg>
    </span>
    <span class="contact-row__text">(412) 555-0148</span>
  </div>
  <div class="contact-row contact-row--big" style="top:178px">
    <span class="contact-row__icon">
      <svg viewBox="0 0 24 24"><path d="M6.6 10.8a15.1 15.1 0 0 0 6.6 6.6l2.2-2.2a1 1 0 0 1 1-.25 11.4 11.4 0 0 0 3.6.57 1 1 0 0 1 1 1V20a1 1 0 0 1-1 1A17 17 0 0 1 3 4a1 1 0 0 1 1-1h3.5a1 1 0 0 1 1 1c0 1.250.2 2.450.57 3.570a1 1 0 0 1-.25 1z"/></svg>
    </span>
    <span class="contact-row__text">(412) 555-0148</span>
  </div>
  <div class="contact-row contact-row--small" style="top:228px">
    <span class="contact-row__icon">
      <svg viewBox="0 0 24 24"><path d="M2 5h20v2l-10 6L2 7zm0 4.3l10 6 10-6V19H2z"/></svg>
    </span>
    <span class="contact-row__text">kontakt@mail.com</span>
  </div>
  <div class="contact-row contact-row--small" style="top:270px">
    <span class="contact-row__icon">
      <svg viewBox="0 0 24 24"><path d="M12 2a10 10 0 1 0 0 20 10 10 0 0 0 0-20zm-1 2.1V8H8.2A8 8 0 0 1 11 4.1zm2 0A8 8 0 0 1 15.8 8H13zM6.3 10H11v4H6.3a8 8 0 0 1 0-4zm6.7 0h4.7a8 8 0 0 1 0 4H13zm-4.8 6H11v3.9A8 8 0 0 1 8.2 16zm4.8 0h2.8A8 8 0 0 1 13 19.9z"/></svg>
    </span>
    <span class="contact-row__text">www.praxisweb.com</span>
  </div>
  <div class="contact-row contact-row--small" style="top:312px">
    <span class="contact-row__icon">
      <svg viewBox="0 0 24 24"><path d="M12 2a7 7 0 0 0-7 7c0 5 7 13 7 13s7-8 7-13a7 7 0 0 0-7-7zm0 9.5A2.5 2.5 0 1 1 12 6.5a2.5 2.5 0 0 1 0 5z"/></svg>
    </span>
    <span class="contact-row__text">27 Lindenweg, 50667</span>
  </div>

  <div class="front-band"></div>
</section>

<section class="card card--back">
  <div class="brand-large">
    <div class="brand-large__mark"></div>
    <p class="brand-large__name">SOMMERFELD<br>CHIRURGIE</p>
  </div>
  <div class="back-rule back-rule--left"></div>
  <p class="back-url">www.praxisweb.com</p>
  <div class="back-rule back-rule--right"></div>
</section>

</body>
</html>
```